Real Estate and Property Management Company needs new listings

We need a business card for our company, Corvell Realty & Property Management. We maximize financial returns on residential investment properties. By evaluating the current value and health of a property, we devise a financial plan to rehabilitate the property while earning an income over a period of years for rental properties, or suggest meaningful updates and improvements to ensure maximum payout on sales properties.
We would like to see our business cards with the colors black and metallic burgundy. The final design should communicate management and financial growth.

Target Market(s)

Home Owners of single family, detatched residential homes.

Industry/Entity Type

Business

Contact Information for Business Card

Side 1: Dana Corvell
Broker, Owner
Dana@CorvellHomesite.example
555-274-8061 (Cell)
555-318-4470 (Office)
Please incorporate in the design of side 1 that we have been in business for 40 years, along with communicating sales and management.
Side 2: Marisa Corvell
Property Manager
Marisa@CorvellHomesite.example
555-274-8095 (Cell)
555-318-4470 (Office)
Please incorporate that we are a family owner and operated company on side 2.

Font styles to use
Serif

Requirements
Must have
• Elegant, feminine design of metallic burgundy on black on double sided card.
Nice to have
• I would like to see some consistency of design on the front and back of the card, with perhaps a bold, thick line of burgundy on the right, vertical side. I would also like the black card stock to have some geometrical design or texture.
Should not have
• Any of the colors provided below. I cannot choose burgundy, which is the color for our business. Is this the only color selection available?

```html
<!DOCTYPE html>
<html lang="en">
<head>
<meta charset="utf-8">
<title>Corvell Realty &amp; Property Management – Business Cards</title>
<link rel="stylesheet" href="https://fonts.googleapis.com/css2?family=Signika:wght@600;700&family=Open+Sans:ital,wght@0,400;0,600;1,400&family=Archivo:wght@700&display=swap">
<style>
  :root {
    --page: #e9e6e3;
    --burgundy-deep: #3a0b0e;
    --burgundy: #5c1217;
    --accent-red: #8e0b10;
    --paper: #ffffff;
    --ink-light: #ffffff;
    --ink-dark: #3a0b0e;
    --divider: #f1e6e6;
  }
  * { box-sizing: border-box; margin: 0; padding: 0; }
  html, body { width: 1200px; height: 900px; overflow: hidden; background: var(--page); }
  .canvas { position: relative; width: 1200px; height: 900px; }

  .card {
    position: absolute;
    left: 250px;
    width: 700px;
    height: 400px;
    overflow: hidden;
    background: radial-gradient(ellipse at 45% 45%, var(--burgundy) 0%, var(--burgundy-deep) 100%);
    box-shadow: 0 6px 18px rgba(0,0,0,0.25);
  }
  .card--back { top: 35px; }
  .card--front { top: 465px; }

  .card__wave { position: absolute; inset: 0; width: 700px; height: 400px; }

  .tagline {
    position: absolute;
    font-family: "Open Sans", sans-serif;
    font-style: italic;
    color: var(--ink-dark);
    line-height: 1.2;
  }
  .card--back .tagline { left: 48px; top: 22px; font-size: 19px; letter-spacing: 0.5px; }
  .card--front .tagline { left: 50px; top: 320px; font-size: 25px; }

  .company {
    position: absolute;
    left: 0; right: 0;
    text-align: center;
    font-family: "Archivo", sans-serif;
    font-weight: 700;
    font-size: 21px;
    letter-spacing: 1.6px;
    color: var(--ink-light);
    text-transform: uppercase;
  }
  .card--back .company { top: 318px; }
  .card--front .company { top: 48px; }

  .person {
    position: absolute;
    right: 370px;
    text-align: right;
    color: var(--ink-light);
  }
  .person__name { font-family: "Signika", sans-serif; font-weight: 700; font-size: 36px; letter-spacing: 1px; line-height: 1.1; }
  .person__role { font-family: "Open Sans", sans-serif; font-size: 19px; letter-spacing: 0.8px; }
  .card--back .person { top: 128px; }
  .card--front .person { top: 138px; }

  .divider { position: absolute; left: 345px; width: 2px; background: var(--divider); }
  .card--back .divider { top: 120px; height: 118px; }
  .card--front .divider { top: 130px; height: 130px; }

  .contacts {
    position: absolute;
    left: 368px;
    list-style: none;
    font-family: "Open Sans", sans-serif;
    color: var(--ink-light);
  }
  .card--back .contacts { top: 126px; font-size: 17px; }
  .card--front .contacts { top: 138px; font-size: 19px; }
  .contacts li { display: flex; align-items: center; gap: 10px; height: 36px; }
  .contacts svg { width: 20px; height: 20px; flex: none; }
</style>
</head>
<body>
<main class="canvas">

  <!-- Side 2: Property Manager -->
  <section class="card card--back">
    <svg class="card__wave" viewBox="0 0 700 400" aria-hidden="true">
      <path d="M0 0 H700 V52 C580 30 470 40 360 62 C240 88 110 100 0 92 Z" fill="var(--accent-red)"/>
      <path d="M0 0 H700 V44 C580 22 470 32 360 54 C240 80 110 92 0 84 Z" fill="var(--paper)"/>
    </svg>
    <p class="tagline">Family owner and<br>operated company</p>
    <div class="person">
      <h2 class="person__name">Marisa Corvell</h2>
      <p class="person__role">Property Manager</p>
    </div>
    <div class="divider"></div>
    <ul class="contacts">
      <li><svg viewBox="0 0 20 20"><circle cx="10" cy="10" r="10" fill="#fff"/><rect x="5" y="6.5" width="10" height="7" fill="var(--burgundy)"/><path d="M5 6.5 L10 10.5 L15 6.5" stroke="#fff" stroke-width="1.2" fill="none"/></svg>Marisa@CorvellHomesite.example</li>
      <li><svg viewBox="0 0 20 20"><circle cx="10" cy="10" r="10" fill="#fff"/><rect x="6.5" y="4.5" width="7" height="11" rx="1.2" fill="var(--burgundy)"/><rect x="8" y="6" width="4" height="6.5" fill="#fff"/></svg>555-274-8095</li>
      <li><svg viewBox="0 0 20 20"><circle cx="10" cy="10" r="10" fill="#fff"/><path d="M6.5 5 L8.5 5 L9.5 8 L8.2 9 C8.8 10.5 9.6 11.3 11 11.9 L12 10.6 L15 11.6 L15 13.6 C15 14.4 14.3 15 13.5 15 C9.4 14.6 5.4 10.6 5 6.5 C5 5.7 5.7 5 6.5 5 Z" fill="var(--burgundy)"/></svg>555-318-4470</li>
    </ul>
    <p class="company">Corvell Realty &amp; Property Management</p>
  </section>

  <!-- Side 1: Broker, Owner -->
  <section class="card card--front">
    <svg class="card__wave" viewBox="0 0 700 400" aria-hidden="true">
      <path d="M0 300 C120 268 250 278 390 312 C510 340 610 340 700 310 V400 H0 Z" fill="var(--accent-red)"/>
      <path d="M0 310 C120 278 250 288 390 322 C510 350 610 350 700 322 V400 H0 Z" fill="var(--paper)"/>
    </svg>
    <p class="company">Corvell Realty &amp; Property Management</p>
    <div class="person">
      <h1 class="person__name">Dana Corvell</h1>
      <p class="person__role">Broker, Owner</p>
    </div>
    <div class="divider"></div>
    <ul class="contacts">
      <li><svg viewBox="0 0 20 20"><circle cx="10" cy="10" r="10" fill="#fff"/><rect x="5" y="6.5" width="10" height="7" fill="var(--burgundy)"/><path d="M5 6.5 L10 10.5 L15 6.5" stroke="#fff" stroke-width="1.2" fill="none"/></svg>Dana@CorvellHomesite.example</li>
      <li><svg viewBox="0 0 20 20"><circle cx="10" cy="10" r="10" fill="#fff"/><rect x="6.5" y="4.5" width="7" height="11" rx="1.2" fill="var(--burgundy)"/><rect x="8" y="6" width="4" height="6.5" fill="#fff"/></svg>555-274-8061</li>
      <li><svg viewBox="0 0 20 20"><circle cx="10" cy="10" r="10" fill="#fff"/><path d="M6.5 5 L8.5 5 L9.5 8 L8.2 9 C8.8 10.5 9.6 11.3 11 11.9 L12 10.6 L15 11.6 L15 13.6 C15 14.4 14.3 15 13.5 15 C9.4 14.6 5.4 10.6 5 6.5 C5 5.7 5.7 5 6.5 5 Z" fill="var(--burgundy)"/></svg>555-318-4470</li>
    </ul>
    <p class="tagline">40 years in business with<br>communicating sales and management</p>
  </section>

</main>
</body>
</html>
```